Financial Retirement Seminar Mailer

We would like to redesign our mailer flyer so that it looks classier and more effective in attracting people to sign up for our events. We help people who are near or in retirement achieve their financial goals.

PLEASE CHANGE THE ENTIRE FORMAT OF THE FLYER AND DO NOT LET IT LOOK SIMILAR TO WHAT WE CURRENTLY HAVE. NOTHING HAS TO STAY THE SAME. THE MORE UNIQUE YOU ARE THE HIGHER YOUR CHANCES OF WINNING.
ALL IMAGES CAN BE CHANGED (except Dorian Feld's photo and the logo for Marlow's Hearth Restaurant)

Target Market(s)

Our Target Market are upper middle class adults nearing or in retirement ages 55+.

Industry/Entity Type

Finance

Font styles to use
Serif
Sans Serif

Colors
0255a3
fece3e
ffffff

Requirements
Must have
• -Must have a photo of Dorian Feld and logo of Marlows Hearth. All other images can be changed.
• -Use our company colors which are navy and GOLD (Please use gold gradients instead of just yellow color)
• -The flyer must be folded in half. The inside can be full page.
Nice to have
• -If you could make the gold color stand out somehow maybe a gradient gold.

```html
<!DOCTYPE html>
<html lang="en">
<head>
<meta charset="utf-8">
<title>Retirement Seminar Mailer</title>
<link href="https://fonts.googleapis.com/css2?family=Tinos:wght@400;700&family=Raleway:ital,wght@0,400;0,600;0,700;1,700&family=Parisienne&display=swap" rel="stylesheet">
<style>
:root{
  --navy:#1b2a5c;
  --navy-deep:#14204a;
  --charcoal:#2e3640;
  --yellow:#f0c22a;
  --gold-a:#b8944a;
  --gold-b:#e9d193;
  --gold-grad:linear-gradient(90deg,#b48f45 0%,#e9d193 55%,#c9a65c 100%);
  --cream:#fbf0d8;
  --ink:#1b2140;
  --stage:#8a8c94;
  --serif:'Tinos',serif;
  --sans:'Raleway',sans-serif;
  --script:'Parisienne',cursive;
}
*{box-sizing:border-box;margin:0;padding:0}
html,body{width:1200px;height:3016px;overflow:hidden}
body{background:var(--stage);position:relative;font-family:var(--sans);color:var(--ink)}
.sheet{position:absolute;background:#fff;box-shadow:0 6px 14px rgba(0,0,0,.35);overflow:hidden}

/* ---------- outside of folded flyer ---------- */
.outside{left:241px;top:64px;width:739px;height:964px}
.fold-front{position:absolute;left:0;top:0;width:739px;height:472px;transform:rotate(180deg);background:#d6d9e0}
.dine-title{position:absolute;left:0;top:0;width:424px;height:80px;padding:14px 0 0 23px;font-family:var(--serif);color:var(--navy);font-size:24px;line-height:28px;letter-spacing:1.5px}
.dine-by{position:absolute;left:2px;top:80px;width:384px;height:32px;background:var(--gold-grad);font-family:var(--serif);font-size:19px;color:var(--navy);padding:4px 0 0 20px;letter-spacing:.5px}
.dine-photo{position:absolute;left:0;top:112px;width:424px;height:282px;background:radial-gradient(circle at 45% 50%,#f4efe4 0 40%,#c9b49a 60%,#7d8da0 100%)}
.event-panel{position:absolute;left:424px;top:0;width:315px;height:394px;background:var(--yellow)}
.date-box{position:absolute;left:17px;top:16px;width:280px;height:187px;background:var(--navy);color:#fff;font-family:var(--serif);text-align:center;clip-path:polygon(0 0,100% 0,100% 88%,50% 100%,0 88%)}
.date-box .day{font-size:20px;line-height:21px;letter-spacing:1px;margin-top:22px}
.date-box .or{display:flex;align-items:center;justify-content:center;gap:10px;margin:12px 0 10px}
.date-box .or span{width:90px;height:2px;background:#fff}
.date-box .or b{background:var(--yellow);color:var(--navy);font-weight:400;font-size:20px;padding:2px 10px}
.date-box .day2{margin-top:0}
.venue-name{position:absolute;left:0;top:222px;width:315px;text-align:center;font-family:var(--serif);font-weight:700;font-size:26px;color:var(--navy);letter-spacing:1px;line-height:28px}
.venue-addr{position:absolute;left:0;top:300px;width:315px;text-align:center;font-family:var(--sans);font-size:15px;line-height:19px;color:var(--ink)}
.confirm-bar{position:absolute;left:0;top:394px;width:739px;height:78px;background:linear-gradient(90deg,var(--navy) 0 57%,var(--charcoal) 57% 100%);color:#fff;font-family:var(--serif);font-weight:700;text-align:center;font-size:19px;line-height:24px;padding-top:15px;letter-spacing:.5px}
.confirm-bar em{font-style:normal;font-weight:400}

.host{position:absolute;left:0;top:472px;width:739px;height:434px;background:var(--navy)}
.host-title{position:absolute;left:28px;top:30px;width:329px;height:44px;border:2px solid var(--gold-a);color:var(--yellow);font-family:var(--serif);font-size:29px;text-align:center;line-height:40px}
.host-bio{position:absolute;left:28px;top:97px;width:405px;color:#e6e8f0;font-size:13px;line-height:18.2px}
.host-bio b{color:#fff}
.host-frame{position:absolute;left:457px;top:21px;width:260px;height:332px;border:2px solid var(--gold-a)}
.host-photo{position:absolute;left:8px;top:8px;width:242px;height:322px;background:linear-gradient(180deg,#f3f3f3 0%,#dcdcdc 55%,#23262e 100%)}
.host-name{position:absolute;left:450px;top:353px;width:278px;height:50px;background:var(--gold-grad);text-align:center;font-family:var(--serif);color:var(--navy)}
.host-name b{display:block;font-size:14px;text-decoration:underline;padding-top:3px}
.host-name span{display:block;font-size:11px;line-height:13px}
.video-bar{position:absolute;left:0;top:356px;width:441px;height:50px;background:var(--gold-grad);font-family:var(--serif);font-weight:700;color:var(--navy);font-size:15.5px;line-height:18px;text-align:center;padding-top:7px}
.featured{position:absolute;left:0;top:906px;width:739px;height:58px;background:var(--cream);display:flex;align-items:center;padding-left:33px;gap:18px}
.featured p{font-family:var(--serif);font-size:11px;line-height:12px;width:120px;color:#333}
.badge{background:#3c4150;border-radius:4px;height:22px}

/* ---------- inside page ---------- */
.inside{left:239px;top:1072px;width:741px;height:967px}
.inside-head{position:absolute;left:0;top:0;width:741px;height:87px;background:var(--navy)}
.inside-head .frame{position:absolute;left:18px;top:19px;width:704px;height:52px;border:1.5px solid var(--yellow);text-align:center;color:#fff;font-family:var(--serif)}
.inside-head h1{font-size:21px;font-weight:400;letter-spacing:1.5px;line-height:24px;margin-top:3px}
.inside-head p{font-size:17px;line-height:19px}
.invite{position:absolute;left:0;top:87px;width:741px;height:470px;background:linear-gradient(180deg,#fff 0%,#fff 30%,#fbe9a8 75%,var(--yellow) 100%)}
.invite-copy{position:absolute;left:23px;top:25px;width:380px;font-size:17.6px;line-height:27.3px;color:#111}
.invite-copy .nosell{margin-top:27px;font-weight:700;font-style:italic;color:var(--navy)}
.enroll{position:absolute;left:18px;top:377px;width:396px;height:61px;background:var(--navy);border:2px solid #fff;outline:1px solid var(--navy);color:#fff;text-align:center;font-family:var(--serif)}
.enroll b{display:block;font-size:21px;font-weight:400;margin-top:6px;line-height:24px}
.enroll span{font-size:15px}
.date-card{position:absolute;left:432px;top:22px;width:287px;height:429px;background:var(--navy)}
.date-card .head{height:34px;background:#1d1f28;color:var(--yellow);font-family:var(--serif);font-size:21px;text-align:center;line-height:34px;letter-spacing:1px}
.date-card .info{height:124px;color:#fff;font-family:var(--serif);font-weight:700;text-align:center;font-size:14.5px;line-height:17.5px;padding-top:7px}
.date-card .info p+p{margin-top:13px}
.venue-photo{position:absolute;left:0;top:158px;width:287px;height:271px;background:linear-gradient(160deg,#5a3b2c 0%,#b48a6a 45%,#e6d6c4 75%,#7a5544 100%)}
.venue-tag{position:absolute;right:8px;top:12px;font-family:var(--serif);font-weight:700;font-size:15px;line-height:17px;color:#fff;text-align:center;width:122px}
.menu-strip{position:absolute;left:0;top:557px;width:741px;height:39px;background:#fff;font-family:var(--serif);font-size:19px;text-align:center;line-height:39px;color:var(--ink)}
.topics{position:absolute;left:0;top:596px;width:741px;height:302px;background:var(--navy)}
.topics-title{position:absolute;left:301px;top:11px;width:139px;height:31px;border:1.5px solid var(--yellow);color:#fff;text-align:center;font-family:var(--serif);font-size:21px;line-height:28px}
.topic{position:absolute;top:129px;width:161px;height:156px;background:var(--yellow);text-align:center}
.topic-img{position:absolute;top:49px;width:117px;height:117px;border-radius:50%;border:3px solid #fff}
.topic h3{font-family:var(--serif);font-weight:400;font-size:17px;line-height:16px;color:var(--navy);margin-top:45px;letter-spacing:.5px}
.topic p{font-size:10.5px;line-height:13.5px;color:#222;margin-top:9px;padding:0 6px}
.register-bar{position:absolute;left:0;top:898px;width:741px;height:46px;background:var(--gold-grad);display:flex;align-items:center;justify-content:center;gap:8px;font-size:15.5px;color:#222}
.register-bar b{color:var(--navy)}
.register-bar svg{width:22px;height:22px}

/* ---------- envelope ---------- */
.envelope{top:2107px;width:531px;height:693px;background:var(--cream)}
.env-front{left:59px}
.env-back{left:626px}
.env-foot{position:absolute;left:0;bottom:0;width:100%;height:28px;background:#fff}
.return-addr{position:absolute;left:18px;top:22px;display:flex;gap:4px;font-family:var(--serif);font-size:11px;line-height:12px;color:#333}
.return-addr svg{width:11px;height:13px;margin-top:-1px}
.stamp{position:absolute;left:431px;top:23px;width:77px;height:82px;border:1.5px solid var(--navy)}
.script{position:absolute;left:0;top:160px;width:531px;text-align:center;font-family:var(--script);font-size:58px;color:#b7944c;line-height:70px}
.enclosed{position:absolute;left:0;top:232px;width:531px;height:34px;border-top:2px solid var(--navy);padding-top:3px}
.enclosed div{height:26px;background:var(--navy);color:var(--cream);text-align:center;font-family:var(--sans);font-size:19px;line-height:26px}
.flap{position:absolute;left:0;top:0;width:531px;height:200px}
.seal{position:absolute;left:207px;top:117px;width:117px;height:117px;border-radius:50%;background:radial-gradient(circle at 40% 35%,#fff3b5 0%,#f0cc3c 50%,#c79c1e 100%);box-shadow:0 0 0 4px #caa22b;display:flex;align-items:center;justify-content:center}
.seal span{width:92px;height:92px;border-radius:50%;border:1.5px solid #8a6a14;display:flex;align-items:center;justify-content:center;font-family:var(--serif);font-size:23px;color:#4a3a10;letter-spacing:1px}
</style>
</head>
<body>

<!-- Outside of the folded flyer -->
<section class="sheet outside">
  <div class="fold-front">
    <div class="dine-title">COMPLIMENTARY DINING &amp;<br>RETIREMENT EDUCATION</div>
    <div class="dine-by">By: Pacific Crest Instructor, DORIAN FELD</div>
    <div class="dine-photo" role="img" aria-label="Seafood pasta dish with mussels and clams in a white bowl"></div>
    <div class="event-panel">
      <div class="date-box">
        <div class="day">TUESDAY<br>08.10.2019 AT 7:00 PM</div>
        <div class="or"><span></span><b>OR</b><span></span></div>
        <div class="day day2">WEDNESDAY<br>09.10.2019 AT 7:00 PM</div>
      </div>
      <div class="venue-name">MARLOW'S<br>HEARTH</div>
      <div class="venue-addr">4820 Linden Cove Ave. #230<br>Seabright, CA 90911<br>(Floor 2)</div>
    </div>
    <div class="confirm-bar">REGISTRATION IS LIMITED! <em>Confirm Today at</em><br>&#9679; 888-555-0142 <em>or Visit</em> &#9679; GOLDENYEARSCLASSES.ORG</div>
  </div>

  <div class="host">
    <div class="host-title">MEET YOUR HOST</div>
    <p class="host-bio">Dorian Feld is a <b>Certified Financial Planner</b>, financial <b>writer for The Ledger Daily</b>, an instructor at <b>Pacific Crest</b> and <b>Steady Wealth Building for Retirement.</b><br>Dorian's understanding of the connection between emotional and financial well being is the catalyst that empowers his clients to take positive action toward improving the quality of their lives and finances for retirement. He works with individuals and families to create wealth, legacy and impact.<br>A regular speaker on KVRN 1150AM and a frequent guest on popular financial shows. Dorian's firm, Harborline Financial exclusively works with people ages 55-67 years old who are in retirement or focused on retiring.</p>
    <div class="host-frame"><div class="host-photo" role="img" aria-label="Portrait of host Dorian Feld in a dark suit and gold tie"></div></div>
    <div class="video-bar">VIEW A VIDEO OF DORIAN ONLINE AND REGISTER<br>AT GOLDENYEARSCLASSES.ORG</div>
    <div class="host-name"><b>DORIAN FELD</b><span>Certified Financial Planner Instructor<br>at Pacific Crest, The Ledger Daily Writer</span></div>
  </div>

  <div class="featured">
    <p>Dorian has been featured in the following and more:</p>
    <div class="badge" style="width:42px"></div>
    <div class="badge" style="width:78px"></div>
    <div class="badge" style="width:22px;border-radius:50%"></div>
    <div class="badge" style="width:90px"></div>
    <div class="badge" style="width:80px"></div>
  </div>
</section>

<!-- Inside page -->
<section class="sheet inside">
  <header class="inside-head">
    <div class="frame">
      <h1>ADVANCED RETIREMENT SOLUTIONS</h1>
      <p>Featuring Pacific Crest Instructor, Dorian Feld, CFP</p>
    </div>
  </header>

  <div class="invite">
    <div class="invite-copy">
      <p>You are invited to an educational talk featuring Pacific Crest instructor Dorian Feld. This FREE* event is focused in teaching the techniques and tools that your financial advisor does not want you to know. Instructor Dorian Feld will cover advanced retirement and tax topics which are proven to be successful and mostly unknown to customers.</p>
      <p class="nosell">Leave your checkbooks at home, there will be no selling here!</p>
    </div>
    <div class="enroll"><b>Early Enrollment is FREE!</b><span>Participants may enroll at door for $99 per seat</span></div>
    <div class="date-card">
      <div class="head">SAVE THE DATE</div>
      <div class="info">
        <p>TUESDAY, 08.10.2019 at 7:00 PM<br>WEDNESDAY, 09.10.2019 at 7:00PM</p>
        <p>4820 Linden Cove Ave. #230<br>Seabright, CA 90911<br>(Floor 2)</p>
      </div>
      <div class="venue-photo" role="img" aria-label="Restaurant private dining room with set tables">
        <div class="venue-tag">MARLOW'S HEARTH</div>
      </div>
    </div>
  </div>

  <div class="menu-strip">Choose from: VEGAN, VEGETARIAN, SEAFOOD, PASTA or STEAK</div>

  <div class="topics">
    <div class="topics-title">TOPICS</div>
    <div class="topic" style="left:18px">
      <h3>LOW-RISK<br>INVESTING</h3>
      <p>New low-risk investments that produce 5%-7% interest and can provide you long term care income. (No Stocks or Bonds)</p>
    </div>
    <div class="topic" style="left:199px">
      <h3>ESTATE<br>PLANNING</h3>
      <p>If you own a home, it's essential to have a Trust in order to avoid probate and to protect yourself if you become disabled.</p>
    </div>
    <div class="topic" style="left:378px">
      <h3>TAX<br>STRATEGIES</h3>
      <p>Learn how to save at least 30% on your 401K Taxes and greatly reduce your taxable income in retirement.</p>
    </div>
    <div class="topic" style="left:560px">
      <h3>LONG TERM<br>CARE</h3>
      <p>Learn how to protect yourself against the high costs of long-term care. Discover 3 new solutions you may not have seen before</p>
    </div>
    <div class="topic-img" style="left:40px;background:linear-gradient(135deg,#dfe9f2,#6f9cc6)" role="img" aria-label="Financial charts and a pen on a desk"></div>
    <div class="topic-img" style="left:221px;background:linear-gradient(135deg,#f1ebe2,#8a5a36)" role="img" aria-label="Gavel resting on a will and testament"></div>
    <div class="topic-img" style="left:400px;background:linear-gradient(135deg,#eeeeee,#b9b2a8)" role="img" aria-label="Smiling senior couple"></div>
    <div class="topic-img" style="left:582px;background:linear-gradient(135deg,#e7f1f7,#5d8db2)" role="img" aria-label="Caregiver with an elderly woman"></div>
  </div>

  <div class="register-bar">
    REGISTER ONLINE AT
    <svg viewBox="0 0 24 24"><circle cx="12" cy="12" r="11" fill="#fff"/><path d="M8 6.5l2 2-1 1.6c.8 1.7 2.2 3.1 3.9 3.9l1.6-1 2 2-1.3 1.8C11 16.5 7.5 13 6.2 7.8z" fill="#1b2a5c"/></svg>
    <b>GOLDENYEARSCLASSES.ORG</b> OR CALL
    <svg viewBox="0 0 24 24"><circle cx="12" cy="12" r="11" fill="#1b2a5c"/><circle cx="12" cy="12" r="6" fill="none" stroke="#fff" stroke-width="1.4"/><path d="M6 12h12M12 6c-2.5 3-2.5 9 0 12M12 6c2.5 3 2.5 9 0 12" fill="none" stroke="#fff" stroke-width="1.2"/></svg>
    <b>888-555-0142</b>
  </div>
</section>

<!-- Envelope front -->
<section class="sheet envelope env-front">
  <div class="return-addr">
    <svg viewBox="0 0 12 14"><path d="M6 0a5 5 0 0 0-5 5c0 3.5 5 9 5 9s5-5.5 5-9a5 5 0 0 0-5-5zm0 7a2 2 0 1 1 0-4 2 2 0 0 1 0 4z" fill="#b7944c"/></svg>
    <p>1780 Orchard Row Suite #1101<br>Lakeport, CA, 90077</p>
  </div>
  <div class="stamp"></div>
  <div class="script">Special Invitation</div>
  <div class="enclosed"><div>IS ENCLOSED</div></div>
  <div class="env-foot"></div>
</section>

<!-- Envelope back -->
<section class="sheet envelope env-back">
  <svg class="flap" viewBox="0 0 531 200"><path d="M6 0 L60 170 L470 170 L525 0" fill="none" stroke="#e3d7bd" stroke-width="2"/></svg>
  <div class="seal"><span>RSVP</span></div>
  <div class="env-foot"></div>
</section>

</body>
</html>
```